Demo Screens Needed for Recruiting with AI App

We are in the process of raising money for our startup called KelvoraLink. We need demos to show investors what we're trying to do with images. We really love the simplicity and modern look of the Pivlo App and want something similar. We will have the "swipe" functionality similar to Flarvi as well. The sample images I've attached are only for caregivers but long term this will be for all industries. There will also be a rewards page for loyalty membership. The current landing page is www.kelvoralink-demo.com. That will show you the color scheme and logo.

```html
<!DOCTYPE html>
<html lang="en">
<head>
<meta charset="utf-8">
<title>KelvoraLink – App Screens</title>
<link href="https://fonts.googleapis.com/css2?family=Urbanist:wght@200;300;400;500;600;700&display=swap" rel="stylesheet">
<style>
:root{
  --bg:#021a24;
  --ink:#0b1a22;
  --accent:#1283b6;
  --accent-bright:#27a9e1;
  --band:#d9f1fb;
  --chip-line:#bfe3f2;
  --icon-tile:#dff2fa;
  --white:#ffffff;
  --muted:#6b7a82;
  --star:#f5b800;
}
*{box-sizing:border-box;margin:0;padding:0}
html,body{width:1200px;height:821px;overflow:hidden}
body{background:var(--bg);font-family:"Urbanist",sans-serif;position:relative;color:var(--ink)}
.screen{position:absolute;top:116px;width:272px;height:590px;border-radius:24px;overflow:hidden;box-shadow:0 0 30px rgba(18,131,182,.18)}
.screen--welcome{left:125px;background:linear-gradient(180deg,#1d4757 0%,#163a49 45%,#0b2430 75%,#061a23 100%)}
.screen--match{left:464px;background:var(--white)}
.screen--detail{left:803px;background:var(--white)}
.status{position:absolute;top:14px;left:0;right:0;height:14px;display:flex;justify-content:space-between;padding:0 26px 0 37px;font-size:11px;font-weight:600}
.status svg{height:10px}
.home-bar{position:absolute;bottom:6px;left:50%;width:96px;height:3px;margin-left:-48px;border-radius:2px;background:var(--ink)}
.photo{position:absolute}
/* welcome */
.screen--welcome .status{color:var(--white)}
.brand{position:absolute;top:278px;left:0;right:0;text-align:center;font-weight:200;font-size:27px;letter-spacing:3px;color:var(--white)}
.tagline{position:absolute;top:324px;left:0;right:0;text-align:center;font-size:17px;font-weight:300;line-height:20px;color:#dfe9ee;letter-spacing:.5px}
.tagline em{font-style:normal;color:var(--accent-bright)}
.btn-create{position:absolute;top:397px;left:51px;width:169px;height:33px;border-radius:17px;background:var(--accent);color:var(--white);font-size:10.5px;font-weight:600;display:flex;align-items:center;justify-content:center;box-shadow:0 0 14px rgba(39,169,225,.45)}
.login-row{position:absolute;top:532px;left:17px;right:18px;height:33px;display:flex;justify-content:space-between;align-items:center;color:var(--white);font-size:11px}
.btn-login{width:79px;height:33px;border-radius:17px;background:#06202b;color:var(--accent-bright);font-weight:700;font-size:11px;display:flex;align-items:center;justify-content:center;gap:6px;box-shadow:0 0 12px rgba(39,169,225,.3)}
.screen--welcome .home-bar{background:var(--white)}
/* match */
.profile-name{position:absolute;top:40px;left:11px;font-size:22px;font-weight:400}
.head-icons{position:absolute;top:45px;right:16px;display:flex;gap:17px}
.head-icons svg{width:16px;height:16px}
.match-photo{top:78px;left:0;width:272px;height:271px;background:radial-gradient(circle at 50% 45%,#b58363 0 22%,#6f6f72 45%,#8b8b8e 100%)}
.online{position:absolute;top:83px;left:6px;width:72px;height:31px;border-radius:16px;background:#06202b;color:var(--accent-bright);font-size:10.5px;font-weight:600;display:flex;align-items:center;gap:7px;padding-left:11px}
.online::before{content:"";width:8px;height:8px;border-radius:50%;background:var(--accent-bright);box-shadow:0 0 0 2px rgba(39,169,225,.35)}
.prompt{position:absolute;top:371px;left:17px;font-size:11px;font-weight:500}
.answer{position:absolute;top:389px;left:17px;width:236px;font-size:17.5px;font-weight:300;line-height:22px}
.actions{position:absolute;left:12px;right:12px;height:33px;display:flex;justify-content:space-between}
.screen--match .actions{top:488px}
.screen--detail .actions{top:532px}
.act{height:33px;border-radius:17px;display:flex;align-items:center;justify-content:center;gap:4px;box-shadow:0 2px 8px rgba(0,0,0,.12)}
.act--pass{width:55px;background:var(--white)}
.act--like{width:55px;background:#06202b}
.act--profile{width:89px;background:var(--white);font-size:10.5px;font-weight:600;letter-spacing:1px}
.chev{font-size:13px;line-height:1}
.nav{position:absolute;top:534px;left:12px;right:12px;display:flex;justify-content:space-between;align-items:center}
.nav-item{width:33px;height:33px;display:flex;align-items:center;justify-content:center;position:relative}
.nav-item svg{width:16px;height:16px}
.nav-item--active{border-radius:50%;background:var(--icon-tile)}
.nav-dot{position:absolute;top:6px;right:6px;width:6px;height:6px;border-radius:50%;background:var(--accent-bright)}
/* detail */
.detail-head{position:absolute;top:34px;left:16px;right:16px;display:flex;justify-content:space-between;align-items:center;font-size:15px;font-weight:500}
.detail-head svg{width:15px;height:15px}
.summary{position:absolute;top:61px;left:0;right:0;height:60px;background:var(--band);padding:9px 17px 0;font-size:11px;line-height:16px;display:flex;justify-content:space-between}
.summary-right{text-align:right}
.stars{color:var(--star);font-size:11px;letter-spacing:1px}
.stars span{color:#d7dde0}
.attributes{position:absolute;top:106px;left:0;right:0;height:260px;background:var(--white);border-radius:18px 18px 0 0;padding:14px 0 0 17px}
.attr-row{display:flex;align-items:center;gap:6px;height:33px}
.attr-icon{width:30px;height:30px;border-radius:6px;background:var(--icon-tile);display:flex;align-items:center;justify-content:center;flex:none}
.attr-icon svg{width:14px;height:14px}
.chip{height:28px;border:1px solid var(--chip-line);border-radius:14px;padding:0 10px;font-size:10px;display:flex;align-items:center;white-space:nowrap}
.detail-photo{top:366px;left:0;width:272px;height:224px;background:radial-gradient(circle at 45% 50%,#c58d6a 0 20%,#7a4a2c 40%,#8d7a68 70%,#b8aa98 100%)}
.scroll-up{position:absolute;top:546px;left:130px;color:var(--white);font-size:10px}
.screen--detail .home-bar{background:var(--white)}
.ico{fill:none;stroke:var(--ink);stroke-width:1.5;stroke-linecap:round;stroke-linejoin:round}
</style>
</head>
<body>

<section class="screen screen--welcome">
  <div class="photo" style="inset:0;background:radial-gradient(ellipse at 60% 30%,rgba(140,150,150,.35),transparent 60%)" role="img" aria-label="Photo of two people leaning close together outdoors"></div>
  <div class="status"><span>9:41</span>
    <svg viewBox="0 0 54 10"><g fill="#fff"><rect x="0" y="6" width="2.5" height="4"/><rect x="4" y="4" width="2.5" height="6"/><rect x="8" y="2" width="2.5" height="8"/><rect x="12" y="0" width="2.5" height="10"/><path d="M22 3a8 8 0 0 1 10 0l-1.3 1.4a6 6 0 0 0-7.4 0zM24.3 5.6a4.5 4.5 0 0 1 5.4 0L27 9z"/><rect x="37" y="1" width="16" height="8" rx="2"/></g></svg>
  </div>
  <div class="brand">KELVORALINK</div>
  <p class="tagline">Unlocking <em>The Power Of</em><br>Meaningful <em>Connections.</em></p>
  <div class="btn-create">CREATE LINK ACCOUNT</div>
  <div class="login-row"><span>Already have an account?</span><span class="btn-login">LOGIN <span>»</span></span></div>
  <div class="home-bar"></div>
</section>

<section class="screen screen--match">
  <div class="status"><span>9:41</span>
    <svg viewBox="0 0 54 10"><g fill="#0b1a22"><rect x="0" y="6" width="2.5" height="4"/><rect x="4" y="4" width="2.5" height="6"/><rect x="8" y="2" width="2.5" height="8"/><rect x="12" y="0" width="2.5" height="10"/><path d="M22 3a8 8 0 0 1 10 0l-1.3 1.4a6 6 0 0 0-7.4 0zM24.3 5.6a4.5 4.5 0 0 1 5.4 0L27 9z"/><rect x="37" y="1" width="16" height="8" rx="2"/></g></svg>
  </div>
  <h1 class="profile-name">Remy</h1>
  <div class="head-icons">
    <svg viewBox="0 0 16 16" class="ico"><path d="M2 3h12v8H6l-3 3v-3H2z"/><path d="M5.5 7h.01M8 7h.01M10.5 7h.01"/></svg>
    <svg viewBox="0 0 16 16" class="ico"><rect x="2" y="2" width="12" height="12" rx="4"/><path d="M5.5 8h.01M8 8h.01M10.5 8h.01"/></svg>
  </div>
  <div class="photo match-photo" role="img" aria-label="Portrait photo of a smiling caregiver"></div>
  <div class="online">Online</div>
  <p class="prompt">One thing I prioritize in childcare is</p>
  <p class="answer">Creating fun and engaging atmosphere where children can explore, play, and express themselves creatively.</p>
  <div class="actions">
    <div class="act act--pass"><svg width="14" height="14" viewBox="0 0 14 14" class="ico"><path d="M2 2l10 10M12 2L2 12"/></svg><span class="chev" style="color:var(--muted)">«</span></div>
    <div class="act act--profile">PROFILE</div>
    <div class="act act--like"><span class="chev" style="color:var(--accent)">»</span><svg width="16" height="14" viewBox="0 0 16 14" class="ico" style="stroke:var(--accent-bright)"><path d="M8 13S1.5 9 1.5 4.5A3.2 3.2 0 0 1 8 3a3.2 3.2 0 0 1 6.5 1.5C14.5 9 8 13 8 13z"/></svg></div>
  </div>
  <nav class="nav">
    <div class="nav-item"><svg viewBox="0 0 16 16" class="ico" style="stroke:var(--muted)"><path d="M8 2L2 14h12zM8 2v12M5 14l3-5 3 5"/></svg></div>
    <div class="nav-item nav-item--active"><svg viewBox="0 0 16 16" class="ico" style="stroke:var(--accent)"><path d="M8 1.5c.6 3.6 2.9 5.9 6.5 6.5-3.6.6-5.9 2.9-6.5 6.5C7.4 10.9 5.1 8.6 1.5 8 5.1 7.4 7.4 5.1 8 1.5z"/></svg></div>
    <div class="nav-item"><svg viewBox="0 0 16 16" class="ico" style="stroke:var(--muted)"><path d="M2 3h12v8H6l-3 3v-3H2z"/><path d="M5.5 7h.01M8 7h.01M10.5 7h.01"/></svg><span class="nav-dot"></span></div>
    <div class="nav-item"><svg viewBox="0 0 16 16" class="ico" style="stroke:var(--muted)"><circle cx="7" cy="7" r="5"/><path d="M11 11l3.5 3.5"/></svg></div>
    <div class="nav-item"><svg viewBox="0 0 16 16" class="ico" style="stroke:var(--muted)"><circle cx="8" cy="5" r="3"/><path d="M2.5 15c0-3.5 2.5-5.5 5.5-5.5s5.5 2 5.5 5.5"/></svg></div>
  </nav>
  <div class="home-bar"></div>
</section>

<section class="screen screen--detail">
  <div class="status"><span>9:41</span>
    <svg viewBox="0 0 54 10"><g fill="#0b1a22"><rect x="0" y="6" width="2.5" height="4"/><rect x="4" y="4" width="2.5" height="6"/><rect x="8" y="2" width="2.5" height="8"/><rect x="12" y="0" width="2.5" height="10"/><path d="M22 3a8 8 0 0 1 10 0l-1.3 1.4a6 6 0 0 0-7.4 0zM24.3 5.6a4.5 4.5 0 0 1 5.4 0L27 9z"/><rect x="37" y="1" width="16" height="8" rx="2"/></g></svg>
  </div>
  <header class="detail-head">
    <svg viewBox="0 0 15 15" class="ico"><path d="M14 7.5H1.5M6 3L1.5 7.5 6 12"/></svg>
    <span>Noa</span>
    <svg viewBox="0 0 16 16" class="ico"><rect x="2" y="2" width="12" height="12" rx="4"/><path d="M5.5 8h.01M8 8h.01M10.5 8h.01"/></svg>
  </header>
  <div class="summary">
    <div>10 yrs experience<br>Female</div>
    <div class="summary-right">$25-$35/hr<br><span class="stars">★★★★<span>★</span></span></div>
  </div>
  <div class="attributes">
    <div class="attr-row"><span class="attr-icon"><svg viewBox="0 0 14 14" class="ico"><path d="M7 13s4.5-4.2 4.5-7.5a4.5 4.5 0 0 0-9 0C2.5 8.8 7 13 7 13z"/><circle cx="7" cy="5.5" r="1.5"/></svg></span><span class="chip">Palo Alto, California</span></div>
    <div class="attr-row"><span class="attr-icon"><svg viewBox="0 0 14 14" class="ico"><circle cx="7" cy="7" r="6"/><path d="M1 7h12M7 1c2 2 2 10 0 12M7 1c-2 2-2 10 0 12"/></svg></span><span class="chip">English</span><span class="chip">Spanish</span><span class="chip">Mandarin</span></div>
    <div class="attr-row"><span class="attr-icon"><svg viewBox="0 0 14 14" class="ico"><path d="M7 1l1.7 1.3 2.1-.1.6 2 1.7 1.3-.7 2 .7 2-1.7 1.3-.6 2-2.1-.1L7 13l-1.7-1.3-2.1.1-.6-2L.9 8.5l.7-2-.7-2 1.7-1.3.6-2 2.1.1z"/><path d="M4.8 7l1.5 1.5L9.2 5.6"/></svg></span><span class="chip">Bachelor’s Degree</span></div>
    <div class="attr-row"><span class="attr-icon"><svg viewBox="0 0 14 14" class="ico"><path d="M1 2h2l1.5 6h7l1-4H4"/><circle cx="5" cy="11.5" r="1.2"/><circle cx="10.5" cy="11.5" r="1.2"/></svg></span><span class="chip">0-11 mo</span><span class="chip">1-3 yrs</span><span class="chip">4-5 yrs</span></div>
    <div class="attr-row"><span class="attr-icon"><svg viewBox="0 0 14 14" class="ico"><rect x="1.5" y="4" width="11" height="8.5" rx="1.5"/><path d="M5 4V2.5h4V4M1.5 7.5h11"/></svg></span><span class="chip">CPR Trained</span><span class="chip">Special Needs Care</span></div>
    <div class="attr-row"><span class="attr-icon"><svg viewBox="0 0 14 14" class="ico"><path d="M12.5 7A5.5 5.5 0 1 1 7 1.5"/><path d="M7 4v3l2 1.5"/></svg></span><span class="chip">Full Time</span><span class="chip">Open to part time</span></div>
    <div class="attr-row"><span class="attr-icon"><svg viewBox="0 0 14 14" class="ico"><circle cx="7" cy="7" r="6"/><path d="M7 4v6M4 7h6"/></svg></span><span class="chip">Comfortable with pets</span><span class="chip">Meals prep</span></div>
  </div>
  <div class="photo detail-photo" role="img" aria-label="Photo of a smiling caregiver with curly hair"></div>
  <span class="scroll-up">︽</span>
  <div class="actions">
    <div class="act act--pass"><svg width="14" height="14" viewBox="0 0 14 14" class="ico"><path d="M2 2l10 10M12 2L2 12"/></svg><span class="chev" style="color:var(--muted)">«</span></div>
    <div class="act act--like"><span class="chev" style="color:var(--accent)">»</span><svg width="16" height="14" viewBox="0 0 16 14" class="ico" style="stroke:var(--accent-bright)"><path d="M8 13S1.5 9 1.5 4.5A3.2 3.2 0 0 1 8 3a3.2 3.2 0 0 1 6.5 1.5C14.5 9 8 13 8 13z"/></svg></div>
  </div>
  <div class="home-bar"></div>
</section>

</body>
</html>
```